Business Card Design

Brightwell Metrics is an Australian company that provides a new monitoring product for solar systems. We are a tech company that needs a professional, corporate business card. Clean lines, no clutter, easy to read and import into contacts.

Can be double sided or single sided - but only want a simple logo on back

Target Market(s)

Professionals and trades. Business community

Industry/Entity Type

Business

Contact Information for Business Card

See email signature image. We need business cards for 2 people (same design)

Requirements
Must have
• Logo.
Contact details

```html
<!DOCTYPE html>
<html lang="en">
<head>
<meta charset="utf-8">
<title>Brightwell Metrics — Business Card</title>
<link rel="stylesheet" href="https://fonts.googleapis.com/css2?family=Open+Sans:wght@400;600&family=EB+Garamond:wght@400&display=swap">
<style>
  :root {
    --backdrop: #6e4226;
    --card: #ffffff;
    --brand-blue: #2a6fa8;
    --brand-gold: #f1b21c;
    --ink: #1c1c1c;
    --rule: #c9c9c9;
    --shadow: rgba(0, 0, 0, 0.35);
  }
  * { box-sizing: border-box; margin: 0; padding: 0; }
  html, body { width: 1200px; height: 498px; overflow: hidden; }
  body {
    background: var(--backdrop);
    font-family: "Open Sans", Arial, sans-serif;
    color: var(--ink);
    position: relative;
  }
  .card {
    position: absolute;
    top: 99px;
    width: 520px;
    height: 300px;
    background: var(--card);
    border-radius: 30px;
    box-shadow: 0 8px 22px var(--shadow);
  }
  .card--front { left: 50px; }
  .card--back { left: 630px; }

  /* Front */
  .brand {
    display: flex;
    align-items: center;
    justify-content: center;
    gap: 12px;
  }
  .brand__square {
    width: 26px;
    height: 26px;
    border-radius: 4px;
    background: var(--brand-gold);
  }
  .brand__name {
    font-family: "Open Sans", Arial, sans-serif;
    font-weight: 600;
    color: var(--brand-blue);
    font-size: 34px;
    letter-spacing: -0.5px;
  }
  .card--front .brand { position: absolute; top: 38px; left: 0; right: 0; }

  .person {
    position: absolute;
    top: 122px;
    left: 0; right: 0;
    text-align: center;
  }
  .person__name { font-size: 20px; }
  .person__role { font-size: 14px; }
  .person__rule {
    width: 230px;
    height: 2px;
    margin: 10px auto 0;
    background: linear-gradient(90deg, transparent, var(--rule) 20%, var(--rule) 80%, transparent);
  }
  .contact {
    position: absolute;
    top: 182px;
    left: 0; right: 0;
    text-align: center;
    font-size: 13.5px;
    line-height: 23px;
  }
  .contact__item { display: inline-flex; align-items: center; gap: 5px; }
  .contact__item + .contact__item { margin-left: 12px; }
  .contact svg { width: 12px; height: 12px; fill: var(--ink); }
  .contact__address { font-size: 14px; margin-top: 6px; }

  /* Back */
  .card--back .brand { position: absolute; top: 86px; left: 0; right: 0; }
  .card--back .brand__square { width: 44px; height: 44px; border-radius: 7px; }
  .card--back .brand__name { font-size: 42px; }
  .back-text {
    position: absolute;
    top: 200px;
    left: 0; right: 0;
    text-align: center;
    font-family: "EB Garamond", Georgia, serif;
    color: var(--ink);
  }
  .back-text__web { font-size: 19px; }
  .back-text__tagline { font-size: 20px; margin-top: 2px; }
</style>
</head>
<body>
  <section class="card card--front" aria-label="Card front">
    <div class="brand">
      <span class="brand__square"></span>
      <span class="brand__name">brightwellmetrics</span>
    </div>
    <div class="person">
      <p><span class="person__name">Lukas Ferrand,</span> <span class="person__role">Managing Director</span></p>
      <div class="person__rule"></div>
    </div>
    <div class="contact">
      <p>
        <span class="contact__item">
          <svg viewBox="0 0 24 24" aria-hidden="true"><path d="M6.6 10.8a15.1 15.1 0 0 0 6.6 6.6l2.2-2.2c.3-.3.7-.4 1-.2 1.1.4 2.3.6 3.6.6.6 0 1 .4 1 1V20c0 .6-.4 1-1 1C10.6 21 3 13.4 3 4c0-.6.4-1 1-1h3.5c.6 0 1 .4 1 1 0 1.3.2 2.5.6 3.6.1.3 0 .7-.2 1z"/></svg>
          61 2 8000 4172
        </span>
        <span class="contact__item">
          <svg viewBox="0 0 24 24" aria-hidden="true"><path d="M7 1h10a2 2 0 0 1 2 2v18a2 2 0 0 1-2 2H7a2 2 0 0 1-2-2V3a2 2 0 0 1 2-2zm0 3v14h10V4zm5 15.5a1.2 1.2 0 1 0 0 2.4 1.2 1.2 0 0 0 0-2.4z"/></svg>
          0400 555 018
        </span>
      </p>
      <p>
        <span class="contact__item">
          <svg viewBox="0 0 24 24" aria-hidden="true"><path d="M2 5h20v14H2zm2 2v.5l8 5 8-5V7zm0 2.8V17h16V9.8l-8 5z"/></svg>
          lukas@brightwellmetrics.com.au
        </span>
      </p>
      <p class="contact__address">A 1204/88 Harbour Rd., Kirribilli NSW 2061 Australia</p>
    </div>
  </section>

  <section class="card card--back" aria-label="Card back">
    <div class="brand">
      <span class="brand__square"></span>
      <span class="brand__name">Brightwell Metrics</span>
    </div>
    <div class="back-text">
      <p class="back-text__web">www.brightwellmetrics.com.au</p>
      <p class="back-text__tagline">Making Sure You Get The Most Out Of Your Solar System</p>
    </div>
  </section>
</body>
</html>
```